Design for company homepage promoting to the pharmaceutical industry

Our company produces medical education materials and services for the pharmaceutical industry. Our existing website (www.quorvan.net.au) provides more information.
 
We need a homepage design for our new company website we are creating. Our site will not have a great amount of content, we want it to be fast, user friendly and easily adaptable to viewing on any platform, and through any browser. We don't want it over-designed - i.e. no highly animated banner flags, backgrounds, obscure webfonts, too many graphics etc. Attached are files indicating our existing company logo and design. We want the logo and rings to be retained. We've also attached draft copy for the website.
The final website may be designed in Wordpress (still to be confirmed)
 
This is a design to replace the current site (www.quorvan.net.au). Content will also be revised.
Things we don't like about our current design - doesn't use our current branding, is not very exciting, old fashioned 'standard' format, too much content, just doesn't look that good, boring.
 
Examples of sites we like:
www.brelmot.com.au
http://factsheets.wondipaq.com.au/index.html
 
Features we like from these sites - fast, responsive, short and to the point, cross-platform compatible including smartphones, and looks good
 
Main reasons people will visit our site: to find out whether we can provide services they might be looking for, to make a decision on whether they are interested in what we offer so they can get in touch with us, and to get our contact details.
Main thing we want to achieve from website visits is that it looks good enough and provides enough summary information on us so that they want to get in touch with us, to offer us work or to ask us to come in and meet them to provide more info on what we do.
Two most important calls to action from our website
· make the decision that we can do what you are looking for
· get in touch with us.
Updates

Thanks everyone for your submissions. At this stage with the Christmas break upon us, we are yet to finalise our decision, and will make a decision early in the new year. I hope everyone has a good holiday break.
Kind regards
Doug

Target Market(s)

Pharmaceutical industry professionals, marketers and medical professionals.

Industry/Entity Type

Pharmaceutical

Requirements
Must have
• Company logo and rings must be incorporated, company colour - blue - must be in there.
Should not have
• Complex animation or graphics that will slow the upload or limit cross-platform compatability/viewing on smartphones etc.

```html
<!DOCTYPE html>
<html lang="en">
<head>
<meta charset="utf-8">
<title>Quorvan – Healthcare Communication Specialists</title>
<link rel="stylesheet" href="https://fonts.googleapis.com/css2?family=Lato:wght@300;400;700&display=swap">
<style>
  :root {
    --brand-blue: #0c4a82;
    --logo-dot: #9aa6c4;
    --ink: #222;
    --muted: #555;
    --panel-grey: #f1f1f1;
    --card-line: #dedede;
    --search-grey: #6b6b6b;
    --bottom-bar: #434247;
    --icon-black: #111;
    --white: #fff;
  }
  * { box-sizing: border-box; margin: 0; padding: 0; }
  html, body { width: 924px; height: 1200px; overflow: hidden; background: var(--white); }
  body { position: relative; font-family: "Lato", Arial, sans-serif; color: var(--ink); }
  .abs { position: absolute; }

  /* Header */
  .brand { left: 115px; top: 24px; display: flex; align-items: center; gap: 8px; }
  .brand-name { font-size: 40px; font-weight: 400; color: var(--brand-blue); letter-spacing: 1px; line-height: 1; }
  .brand-dot { width: 8px; height: 8px; border-radius: 50%; background: var(--logo-dot); }
  .search { left: 699px; top: 15px; width: 138px; height: 20px; display: flex; }
  .search-field { flex: 1; background: var(--search-grey); color: #eee; font-size: 11px; padding: 3px 8px; }
  .search-btn { width: 18px; background: var(--brand-blue); display: flex; align-items: center; justify-content: center; }
  .main-nav { top: 59px; left: 0; width: 924px; height: 38px; }
  .main-nav a { position: absolute; font-size: 10.5px; letter-spacing: 1.2px; color: var(--ink); text-decoration: none; }
  .main-nav a.active::after { content: ""; position: absolute; left: 0; right: 0; top: 34px; height: 4px; background: var(--brand-blue); }

  /* Hero */
  .hero { left: 9px; top: 97px; width: 906px; height: 385px;
    background: radial-gradient(ellipse 60% 35% at 50% 62%, #7f9fb6 0%, #a9c5d8 35%, #c7dcea 65%, #d9e8f2 100%); }
  .hero-line { background: rgba(12,74,130,0.92); color: var(--white); font-size: 20px; font-weight: 300; padding: 4px 0; text-align: center; white-space: nowrap; height: 33px; line-height: 25px; }
  .hero-arrow { top: 284px; }
  .hero-band { left: 9px; top: 482px; width: 906px; height: 5px; background: var(--brand-blue); }

  /* Services */
  .services { left: 9px; top: 487px; width: 906px; height: 286px; background: var(--panel-grey); }
  .service-card { top: 524px; width: 240px; height: 222px; background: var(--white); border: 1px solid var(--card-line); text-align: center; }
  .service-icon { display: block; margin: 40px auto 0; width: 44px; height: 44px; }
  .service-title { margin-top: 17px; font-size: 17px; font-weight: 400; color: var(--brand-blue); line-height: 20px; }
  .service-text { margin-top: 19px; font-size: 11.5px; line-height: 14px; color: var(--muted); padding: 0 20px; }

  /* Clients */
  .section-rule { top: 815px; height: 1px; background: var(--brand-blue); }
  .section-title { left: 0; width: 924px; top: 804px; text-align: center; font-size: 19px; font-weight: 400; letter-spacing: 1px; color: var(--brand-blue); }
  .client-row { top: 876px; left: 140px; width: 650px; display: flex; justify-content: space-between; align-items: center; }
  .client-name { font-size: 18px; font-weight: 700; color: #4a4a4a; display: flex; align-items: center; gap: 6px; }
  .client-mark { width: 10px; height: 10px; border-radius: 50%; background: #4a4a4a; }

  /* Footer */
  .footer { left: 9px; top: 973px; width: 906px; height: 178px; background: var(--brand-blue); color: var(--white); }
  .footer-col { top: 1004px; width: 240px; color: var(--white); }
  .footer-title { font-size: 11px; font-weight: 700; margin-bottom: 12px; }
  .tweet { display: flex; gap: 13px; margin-bottom: 8px; font-size: 8px; line-height: 11px; font-weight: 700; }
  .tweet-mark { flex: none; width: 14px; height: 14px; border-radius: 50%; background: var(--white); margin-top: 3px; }
  .tweet-age { display: block; font-size: 5px; font-weight: 400; opacity: .8; }
  .footer-text { font-size: 7.5px; line-height: 12px; }
  .newsletter-field { margin-top: 9px; width: 145px; height: 16px; display: flex; align-items: center; }
  .newsletter-line { flex: 1; align-self: flex-end; height: 1px; background: var(--white); margin-right: 2px; }
  .newsletter-send { flex: none; width: 14px; height: 13px; background: var(--icon-black); display: flex; align-items: center; justify-content: center; }
  .social { display: flex; gap: 2px; }
  .social span { background: var(--icon-black); height: 22px; padding: 0 4px; font-size: 7px; line-height: 22px; font-weight: 700; }
  .contact-item { display: flex; gap: 10px; margin-bottom: 12px; font-size: 7.5px; line-height: 11px; }
  .contact-icon { flex: none; width: 16px; height: 16px; background: var(--icon-black); display: flex; align-items: center; justify-content: center; }
  .contact-item a { color: var(--white); }

  .bottom-bar { left: 9px; top: 1151px; width: 906px; height: 39px; background: var(--bottom-bar); color: var(--white); font-size: 7.5px; font-weight: 700; padding: 15px 0 0 78px; }
</style>
</head>
<body>

<header>
  <div class="brand abs"><span class="brand-name">quorvan</span><span class="brand-dot"></span></div>
  <div class="search abs">
    <span class="search-field">Search Me</span>
    <span class="search-btn"><svg width="8" height="8" viewBox="0 0 8 8"><circle cx="3.2" cy="3.2" r="2.3" fill="none" stroke="#fff" stroke-width="1.2"/><line x1="5" y1="5" x2="7.4" y2="7.4" stroke="#fff" stroke-width="1.4"/></svg></span>
  </div>
  <nav class="main-nav abs">
    <a class="active" style="left:310px">HOME</a>
    <a style="left:373px">WHO WE ARE</a>
    <a style="left:473px">WHAT WE DO</a>
    <a style="left:572px">OUR WORK</a>
    <a style="left:664px">OUR CLIENT</a>
    <a style="left:754px">CONTACT US</a>
  </nav>
</header>

<section>
  <div class="hero abs" role="img" aria-label="Photograph of ripples spreading across calm blue water"></div>
  <div class="hero-line abs" style="left:163px;top:257px;width:600px;letter-spacing:1.45px">At Quorvan we are healthcare communication specialists;</div>
  <div class="hero-line abs" style="left:91px;top:299px;width:743px;letter-spacing:1.85px">this means we’re scientists, journalists and marketers rolled into one.</div>
  <svg class="hero-arrow abs" style="left:14px" width="10" height="18" viewBox="0 0 10 18"><polyline points="9,1 1,9 9,17" fill="none" stroke="#1f4f80" stroke-width="1.3"/></svg>
  <svg class="hero-arrow abs" style="left:901px" width="10" height="18" viewBox="0 0 10 18"><polyline points="1,1 9,9 1,17" fill="none" stroke="#1f4f80" stroke-width="1.3"/></svg>
  <div class="hero-band abs"></div>
</section>

<section>
  <div class="services abs"></div>
  <svg class="abs" style="left:446px;top:486px" width="30" height="18" viewBox="0 0 30 18"><path d="M0 0 H30 Q18 4 15 18 Q12 4 0 0Z" fill="#0c4a82"/></svg>

  <article class="service-card abs" style="left:85px">
    <div class="service-icon" role="img" aria-label="Icon of a person" style="width:38px;height:42px;margin-bottom:2px;background:#333;border-radius:19px 19px 4px 4px"></div>
    <h2 class="service-title">WHO WE ARE</h2>
    <p class="service-text">Lorem ipsum dolor a sit eget amet, consectetur adipiscing elit in sit amet aliquet odio, nec vehicula leo.</p>
  </article>
  <article class="service-card abs" style="left:341px">
    <svg class="service-icon" viewBox="0 0 44 44"><rect x="8" y="4" width="28" height="38" fill="none" stroke="#333" stroke-width="3"/><rect x="15" y="1" width="14" height="6" fill="#333"/><g stroke="#333" stroke-width="2"><line x1="13" y1="15" x2="31" y2="15"/><line x1="13" y1="21" x2="31" y2="21"/><line x1="13" y1="27" x2="31" y2="27"/><line x1="13" y1="33" x2="25" y2="33"/></g></svg>
    <h2 class="service-title">WHAT WE DO</h2>
    <p class="service-text">Lorem ipsum dolor a sit eget amet, consectetur adipiscing elit in sit amet aliquet odio, nec vehicula leo.</p>
  </article>
  <article class="service-card abs" style="left:598px">
    <svg class="service-icon" viewBox="0 0 44 44"><g fill="#333"><rect x="8" y="4" width="28" height="7" rx="2"/><rect x="6" y="13" width="30" height="7" rx="2"/><rect x="9" y="22" width="28" height="7" rx="2"/><rect x="6" y="31" width="32" height="8" rx="2"/></g></svg>
    <h2 class="service-title">OUR WORK</h2>
    <p class="service-text">Lorem ipsum dolor a sit eget amet, consectetur adipiscing elit in sit amet aliquet odio, nec vehicula leo.</p>
  </article>
  <svg class="abs" style="left:448px;top:773px" width="26" height="14" viewBox="0 0 26 14"><path d="M0 0 H26 Q16 3 13 14 Q10 3 0 0Z" fill="#f1f1f1"/></svg>
</section>

<section>
  <div class="section-rule abs" style="left:85px;width:320px"></div>
  <div class="section-rule abs" style="left:517px;width:320px"></div>
  <h2 class="section-title abs">CLIENTS</h2>
  <div class="client-row abs">
    <span class="client-name"><span class="client-mark"></span>Alvenor</span>
    <span class="client-name">Maudrey</span>
    <span class="client-name"><span class="client-mark"></span>Kestrolo</span>
    <span class="client-name">Veltrana</span>
    <span class="client-name">Pendwise</span>
  </div>
</section>

<footer>
  <div class="footer abs"></div>

  <div class="footer-col abs" style="left:85px">
    <h3 class="footer-title">Latest tweets</h3>
    <div class="tweet"><span class="tweet-mark"></span><span>Check Out Jvanlo’s @Brikboard Sales Notification<br>http://snip.to/ WBFKIWHJ<span class="tweet-age">3 days ago</span></span></div>
    <div class="tweet"><span class="tweet-mark"></span><span>Community Superstar Winner – #MeadowHiveMedia<br>http://snip.to/2Fs1nnMj<span class="tweet-age">3 days ago</span></span></div>
    <div class="tweet"><span class="tweet-mark"></span><span>Clean #Websites Designs for Your #Inspiration<br>http://snip.to/ 5nRKu3HJ<span class="tweet-age">3 days ago</span></span></div>
  </div>

  <div class="footer-col abs" style="left:341px">
    <h3 class="footer-title" style="margin-bottom:8px">Newsletter</h3>
    <p class="footer-text">Lorem Ipsum is simply dummy text of the printing<br>and typesetting industry.</p>
    <div class="newsletter-field"><span class="newsletter-line"></span><span class="newsletter-send"><svg width="9" height="7" viewBox="0 0 9 7"><rect x=".5" y=".5" width="8" height="6" fill="none" stroke="#fff"/><polyline points=".5,.5 4.5,4 8.5,.5" fill="none" stroke="#fff"/></svg></span></div>
    <h3 class="footer-title" style="margin-top:22px;margin-bottom:9px">Social Connecting</h3>
    <div class="social"><span>Frendlo</span><span>Circlo</span><span>Chirpa</span></div>
  </div>

  <div class="footer-col abs" style="left:598px">
    <h3 class="footer-title" style="margin-bottom:18px">Contact info</h3>
    <div class="contact-item"><span class="contact-icon"><svg width="7" height="10" viewBox="0 0 7 10"><path d="M3.5 0A3.5 3.5 0 0 0 0 3.5C0 6 3.5 10 3.5 10S7 6 7 3.5A3.5 3.5 0 0 0 3.5 0Z" fill="#fff"/><circle cx="3.5" cy="3.5" r="1.3" fill="#111"/></svg></span><span>Address: 4812 Rue des Tilleuls Verts,<br>69000 Lyon, France</span></div>
    <div class="contact-item"><span class="contact-icon"><svg width="10" height="10" viewBox="0 0 10 10"><path d="M2 1 L4 3 L3 4.5 Q4.5 6 5.5 7 L7 6 L9 8 L7.5 9.5 Q1 8 .5 2.5Z" fill="#fff"/></svg></span><span>Phone: +38 041 620-17-33<br>&nbsp;&nbsp;&nbsp;&nbsp;&nbsp;&nbsp;&nbsp;&nbsp;&nbsp;&nbsp;&nbsp;&nbsp;+38 041 620-17-34</span></div>
    <div class="contact-item" style="margin-top:6px"><span class="contact-icon"><svg width="10" height="8" viewBox="0 0 10 8"><rect width="10" height="8" fill="#fff"/><polyline points="0,0 5,4.5 10,0" fill="none" stroke="#111"/></svg></span><span style="padding-top:3px">E-mail: <a href="mailto:support@quorvan.net.au">support@quorvan.net.au</a></span></div>
  </div>

  <div class="bottom-bar abs">Copyright 2013 - www.quorvan.com - All Rights Reserved</div>
</footer>

</body>
</html>
```